Need high-end luxury business cards with raised element of logo

Looking for a non-standard business card with the option of part of our logo elements to be printed as raised or embossed. Would like at least 5 different photos on the backside. Looking at printing through this: https://www.cardvellox.com/raised-spot-uv-business-cards.html

updated the logo file

```html
<!DOCTYPE html>
<html lang="en">
<head>
<meta charset="utf-8">
<title>Larchmere Ave – Business Card</title>
<link rel="stylesheet" href="https://fonts.googleapis.com/css2?family=Lato:wght@400;700&family=Oswald:wght@500&display=swap">
<style>
  :root {
    --page-bg: #1c1d1f;
    --card-bg: #111214;
    --steel-blue: #4b6b86;
    --band-blue: #46647d;
    --text-light: #f2f2f2;
    --photo-forest: linear-gradient(135deg, #c98a2a, #5f7a2c 55%, #2f4a22);
    --photo-lodge: linear-gradient(135deg, #6b3410, #c2682a 50%, #3a1f10);
    --photo-pool: linear-gradient(135deg, #3b4d7a, #2fb6c4 60%, #1b2a33);
    --photo-porch: linear-gradient(135deg, #7a3a1a, #d98a3a 50%, #3a2a22);
  }
  html, body {
    margin: 0;
    width: 1200px;
    height: 900px;
    overflow: hidden;
    background: var(--page-bg);
  }
  .canvas {
    position: relative;
    width: 1200px;
    height: 900px;
  }
  .card {
    position: absolute;
    left: 250px;
    width: 700px;
    height: 400px;
    background: var(--card-bg);
    overflow: hidden;
    box-shadow: 0 10px 30px rgba(0,0,0,.5);
  }
  .card--front { top: 40px; }
  .card--back { top: 470px; }

  .card__band {
    position: absolute;
    left: 0; right: 0; bottom: 0;
    height: 22px;
    background: var(--band-blue);
  }

  /* Front */
  .brand {
    position: absolute;
    top: 95px;
    left: 0; right: 0;
    display: flex;
    justify-content: center;
    align-items: center;
    gap: 16px;
  }
  .brand__dot {
    width: 22px;
    height: 22px;
    border-radius: 50%;
    background: var(--steel-blue);
  }
  .brand__name {
    font-family: "Lato", sans-serif;
    font-weight: 400;
    font-size: 52px;
    letter-spacing: 10px;
    color: var(--steel-blue);
    text-transform: uppercase;
  }
  .photo-strip {
    position: absolute;
    left: 0; right: 0;
    top: 235px;
    height: 143px;
    display: grid;
    grid-template-columns: repeat(4, 1fr);
    gap: 2px;
  }
  .photo { height: 100%; }
  .photo--forest { background: var(--photo-forest); }
  .photo--lodge { background: var(--photo-lodge); }
  .photo--pool { background: var(--photo-pool); }
  .photo--porch { background: var(--photo-porch); }

  /* Back */
  .person {
    position: absolute;
    left: 60px;
    top: 150px;
    width: 250px;
    text-align: right;
  }
  .person__name {
    font-family: "Oswald", sans-serif;
    font-weight: 500;
    font-size: 38px;
    line-height: 1;
    color: var(--steel-blue);
    text-transform: uppercase;
    margin: 0;
  }
  .person__title {
    font-family: "Lato", sans-serif;
    font-size: 21px;
    color: var(--text-light);
    margin: 6px 0 0;
  }
  .divider {
    position: absolute;
    left: 330px;
    top: 140px;
    width: 1px;
    height: 100px;
    background: #8a8d92;
  }
  .contacts {
    position: absolute;
    left: 355px;
    top: 145px;
    margin: 0;
    padding: 0;
    list-style: none;
    font-family: "Lato", sans-serif;
    font-size: 21px;
    color: var(--text-light);
  }
  .contacts__item {
    display: flex;
    align-items: center;
    gap: 10px;
    height: 31px;
  }
  .contacts__icon {
    width: 20px;
    height: 20px;
    flex: none;
    color: var(--steel-blue);
  }
  .address {
    position: absolute;
    left: 0; right: 0;
    top: 318px;
    text-align: center;
    font-family: "Lato", sans-serif;
    font-size: 22px;
    color: var(--text-light);
    margin: 0;
  }
</style>
</head>
<body>
<main class="canvas">

  <section class="card card--front" aria-label="Card front">
    <div class="brand">
      <span class="brand__dot"></span>
      <span class="brand__name">Larchmere Ave</span>
    </div>
    <div class="photo-strip">
      <div class="photo photo--forest" role="img" aria-label="Aerial photo of a home among autumn forest"></div>
      <div class="photo photo--lodge" role="img" aria-label="Photo of a wood-panelled lodge living room with stone fireplace"></div>
      <div class="photo photo--pool" role="img" aria-label="Photo of a lit hot tub on a covered deck at dusk"></div>
      <div class="photo photo--porch" role="img" aria-label="Photo of a porch lounge overlooking mountains at sunset"></div>
    </div>
    <div class="card__band"></div>
  </section>

  <section class="card card--back" aria-label="Card back">
    <div class="person">
      <h1 class="person__name">Daniel Whitcombe</h1>
      <p class="person__title">Managing Director</p>
    </div>
    <div class="divider"></div>
    <ul class="contacts">
      <li class="contacts__item">
        <svg class="contacts__icon" viewBox="0 0 24 24" fill="currentColor" aria-hidden="true">
          <path d="M6.6 10.8a15.1 15.1 0 0 0 6.6 6.6l2.2-2.2a1 1 0 0 1 1-.25 11.4 11.4 0 0 0 3.6.57 1 1 0 0 1 1 1V20a1 1 0 0 1-1 1A17 17 0 0 1 3 4a1 1 0 0 1 1-1h3.5a1 1 0 0 1 1 1c0 1.25.2 2.45.57 3.57a1 1 0 0 1-.25 1z"/>
        </svg>
        044-987 210 635
      </li>
      <li class="contacts__item">
        <svg class="contacts__icon" viewBox="0 0 24 24" fill="none" stroke="currentColor" stroke-width="2" aria-hidden="true">
          <rect x="2" y="5" width="20" height="14"/>
          <path d="M2 5l10 8 10-8"/>
        </svg>
        hello@larchmereave.com
      </li>
      <li class="contacts__item">
        <svg class="contacts__icon" viewBox="0 0 24 24" fill="none" stroke="currentColor" stroke-width="1.8" aria-hidden="true">
          <circle cx="12" cy="12" r="10"/>
          <path d="M2 12h20M12 2c3 3 3 17 0 20M12 2c-3 3-3 17 0 20"/>
        </svg>
        www.larchmereave.com
      </li>
    </ul>
    <p class="address">118, Ridgeview Lane, Northvale, 60731</p>
    <div class="card__band"></div>
  </section>

</main>
</body>
</html>
```